TriFold design for a new healthcare company

Looking for a modern design based off some of our older in clinic designs. This is for a start up in which physicians, podiatrists, visit patients in the home called HearthMeds. Logo and wording attached with some stock photos for guidance but not required. Also open to redesigning the logo. QR code also uploaded to be incorporated.

Industry/Entity Type

Healthcare

Colors
0054AA
0677BA
7BADD7
CADEEF
E8F1F8
0094D4
00A9DD
6FCCEA
C7EBF8
E9F6FB

```html
<!DOCTYPE html>
<html lang="en">
<head>
<meta charset="utf-8">
<title>HearthMeds Trifold</title>
<link href="https://fonts.googleapis.com/css2?family=Montserrat:wght@400;500;600;700;800&display=swap" rel="stylesheet">
<style>
  :root{
    --navy:#0054AA;
    --royal:#0a4fb8;
    --mid:#0677BA;
    --sky:#7BADD7;
    --pale:#CADEEF;
    --mist:#E8F1F8;
    --white:#ffffff;
    --ink:#1d2b3a;
    --page:#eef1f4;
  }
  *{box-sizing:border-box;margin:0;padding:0}
  html,body{width:896px;height:1200px;overflow:hidden}
  body{background:var(--page);font-family:"Montserrat",Arial,sans-serif;position:relative}
  .sheet{position:absolute;left:81px;width:733px;height:517px;background:var(--white);overflow:hidden}
  .sheet--outside{top:59px}
  .sheet--inside{top:622px}
  .sheet__art{position:absolute;inset:0}
  .block{position:absolute}
  .pill{display:inline-block;background:var(--white);color:var(--navy);font-weight:700;font-size:13.5px;border-radius:20px;padding:2px 10px 3px;line-height:16px}
  .pill--dark{background:var(--navy);color:var(--white)}
  .on-blue{color:var(--white)}
  .info-list{list-style:none}
  .info-list li{display:flex;gap:8px;align-items:flex-start;font-size:10.2px;line-height:12.5px;margin-bottom:12px}
  .info-list .ring{flex:0 0 24px;height:24px;border:1.5px solid var(--white);border-radius:50%;display:flex;align-items:center;justify-content:center;margin-top:1px}
  .info-list b{font-weight:700}
  .ticks{list-style:none}
  .ticks li{display:flex;gap:8px;font-size:10.3px;line-height:12.5px}
  .ticks svg{flex:0 0 11px;height:11px;margin-top:1px}
  .cta{text-align:center;width:245px;left:244px}
  .cta h2{font-weight:800;font-size:20.5px;line-height:23.5px;color:var(--white);letter-spacing:.3px}
  .contact{position:absolute;left:0;width:245px;text-align:center;color:var(--white)}
  .contact__phone{font-weight:700;font-size:13px}
  .contact__line{font-size:11.5px}
  .contact__line b{font-weight:700}
  .brand{left:489px;width:244px;top:82px;display:flex;align-items:center;justify-content:center;gap:8px}
  .brand__mark{width:18px;height:18px;border-radius:50%;background:var(--sky)}
  .brand__name{font-weight:500;font-size:18px;color:var(--mid);letter-spacing:.5px}
  .tagline{left:489px;width:244px;top:410px;text-align:center;color:var(--white)}
  .tagline__lead{font-weight:500;font-size:16.5px;line-height:20px}
  .tagline__big{font-weight:800;font-size:29px;line-height:30px;letter-spacing:.5px}
  .tagline__pill{display:inline-block;background:var(--white);color:var(--navy);font-weight:600;font-size:14.5px;letter-spacing:2px;border-radius:20px;padding:1px 12px 2px;margin-top:2px}
  .tagline__url{font-size:8px;letter-spacing:1px;margin-top:9px}
  .details p{font-size:10.2px;line-height:12.5px;color:var(--white);margin-bottom:10px}
  .details b{font-weight:700}
</style>
</head>
<body>
<svg width="0" height="0" style="position:absolute" aria-hidden="true">
  <symbol id="tick-blue" viewBox="0 0 12 12"><circle cx="6" cy="6" r="5" fill="none" stroke="#0054AA" stroke-width="1.4"/><path d="M3.2 6.2l2 2 5-5.6" fill="none" stroke="#0054AA" stroke-width="1.8" stroke-linecap="round"/></symbol>
  <symbol id="tick-white" viewBox="0 0 12 12"><circle cx="6" cy="6" r="5" fill="none" stroke="#fff" stroke-width="1.4"/><path d="M3.2 6.2l2 2 5-5.6" fill="none" stroke="#fff" stroke-width="1.8" stroke-linecap="round"/></symbol>
</svg>

<!-- Outside spread -->
<section class="sheet sheet--outside">
  <svg class="sheet__art" viewBox="0 0 733 517" width="733" height="517">
    <defs>
      <linearGradient id="blueFill" x1="0" y1="0" x2="0" y2="1"><stop offset="0" stop-color="#0d58c0"/><stop offset="1" stop-color="#0a47a8"/></linearGradient>
      <linearGradient id="photoGrey" x1="0" y1="0" x2="1" y2="1"><stop offset="0" stop-color="#e3e8ec"/><stop offset="1" stop-color="#b9c4cc"/></linearGradient>
      <linearGradient id="photoSkin" x1="0" y1="0" x2="1" y2="1"><stop offset="0" stop-color="#dfe3e8"/><stop offset="1" stop-color="#e6c9bd"/></linearGradient>
    </defs>
    <g role="img" aria-label="Podiatrist in mask and gloves treating a patient's foot">
      <rect x="0" y="0" width="245" height="330" fill="url(#photoGrey)"/>
    </g>
    <g role="img" aria-label="Gloved hands filing a toenail">
      <rect x="244" y="0" width="245" height="300" fill="url(#photoSkin)"/>
    </g>
    <path d="M0 256 C60 296,110 316,170 296 C230 276,260 222,330 218 C400 214,450 248,510 276 C590 300,670 258,733 224 L733 517 L0 517Z" fill="var(--sky)"/>
    <path d="M0 264 C60 304,110 324,170 304 C230 284,260 230,330 226 C400 222,450 256,510 284 C590 308,670 266,733 232 L733 517 L0 517Z" fill="url(#blueFill)"/>
    <line x1="244.5" y1="0" x2="244.5" y2="517" stroke="#0a47a8" stroke-opacity=".15"/>
    <line x1="489" y1="0" x2="489" y2="517" stroke="#0a47a8" stroke-opacity=".15"/>
    <g role="img" aria-label="Doctor reviewing a tablet with a smiling patient">
      <circle cx="638" cy="247" r="98" fill="#d9dde0" stroke="var(--sky)" stroke-width="5"/>
    </g>
    <g role="img" aria-label="Gloved hands trimming a toenail">
      <circle cx="568" cy="327" r="66" fill="#c9d9e6" stroke="var(--white)" stroke-width="4"/>
      <circle cx="568" cy="327" r="71" fill="none" stroke="var(--pale)" stroke-width="2"/>
    </g>
    <!-- contact rules -->
    <g stroke="#fff" stroke-width="1" fill="none">
      <line x1="282" y1="362" x2="353" y2="362"/><line x1="381" y1="362" x2="453" y2="362"/>
      <line x1="282" y1="415" x2="353" y2="415"/><line x1="381" y1="415" x2="453" y2="415"/>
      <line x1="282" y1="468" x2="353" y2="468"/><line x1="381" y1="468" x2="453" y2="468"/>
      <circle cx="367" cy="362" r="11" stroke-width="1.6"/>
      <circle cx="367" cy="415" r="11" stroke-width="1.6"/>
      <circle cx="367" cy="468" r="11" stroke-width="1.6"/>
      <path d="M362.5 357.5c0 5 4 9 9 9l1.5-2-2.5-1.5-1.3 1a5 5 0 0 1-2.8-2.8l1-1.3-1.5-2.5z" fill="#fff" stroke="none"/>
      <circle cx="367" cy="415" r="5.5" stroke-width="1.2"/>
      <ellipse cx="367" cy="415" rx="2.4" ry="5.5" stroke-width="1"/>
      <line x1="361.5" y1="415" x2="372.5" y2="415" stroke-width="1"/>
      <rect x="361.5" y="464" width="11" height="8" rx="1" fill="#fff" stroke="none"/>
      <path d="M361.5 464.5l5.5 4 5.5-4" stroke="#0a47a8" stroke-width="1.1"/>
    </g>
  </svg>

  <div class="block" style="left:14px;top:332px"><span class="pill">When &amp; Where:</span></div>
  <ul class="block info-list on-blue" style="left:14px;top:374px;width:225px">
    <li><span class="ring"><svg width="12" height="12" viewBox="0 0 12 12"><circle cx="6" cy="6" r="5" fill="none" stroke="#fff" stroke-width="1.2"/><path d="M6 3v3l2 1.5" stroke="#fff" stroke-width="1.2" fill="none"/></svg></span><span><b>Hours :</b> 9am-5pm, Mon-Fri, and occasional Saturdays.</span></li>
    <li><span class="ring"><svg width="12" height="12" viewBox="0 0 12 12"><rect x="1.5" y="2.5" width="9" height="8" rx="1" fill="none" stroke="#fff" stroke-width="1.1"/><line x1="1.5" y1="5" x2="10.5" y2="5" stroke="#fff"/></svg></span><span><b>Appointments :</b> See a doctor usually within 7-10 days of inquiry.</span></li>
    <li><span class="ring"><svg width="12" height="12" viewBox="0 0 12 12"><path d="M6 11s4-4 4-6.5a4 4 0 0 0-8 0C2 7 6 11 6 11z" fill="none" stroke="#fff" stroke-width="1.1"/><circle cx="6" cy="4.6" r="1.4" fill="#fff"/></svg></span><span><b>Coverage Area :</b> North Houston, Katy, Cypress, Willis, Huntsville, east of Lake Houston.</span></li>
  </ul>

  <div class="block cta" style="top:264px"><h2>BOOK YOUR<br>APPOINTMENT<br>TODAY!</h2></div>
  <div class="block" style="left:244px;top:0;width:245px;height:517px">
    <div class="contact contact__phone" style="top:377px">555-014-2290</div>
    <div class="contact contact__line" style="top:432px">www.<b>HearthMeds</b>.com</div>
    <div class="contact contact__line" style="top:485px">info@<b>hearthmeds</b>.com</div>
  </div>

  <div class="block brand"><span class="brand__mark"></span><span class="brand__name">HEARTHMEDS</span></div>

  <div class="block tagline">
    <div class="tagline__lead">Bringing specialized</div>
    <div class="tagline__big">FOOT CARE</div>
    <div class="tagline__pill">to your doorstep</div>
    <div class="tagline__url">www.homefootcarenorth.com</div>
  </div>
</section>

<!-- Inside spread -->
<section class="sheet sheet--inside">
  <svg class="sheet__art" viewBox="0 0 733 517" width="733" height="517">
    <defs>
      <linearGradient id="blueFill2" x1="0" y1="0" x2="0" y2="1"><stop offset="0" stop-color="#0d58c0"/><stop offset="1" stop-color="#0a47a8"/></linearGradient>
      <linearGradient id="photoClinic" x1="0" y1="0" x2="1" y2="1"><stop offset="0" stop-color="#e8e9ea"/><stop offset="1" stop-color="#c7cdd2"/></linearGradient>
      <linearGradient id="photoFoot" x1="0" y1="0" x2="1" y2="1"><stop offset="0" stop-color="#e4e9ee"/><stop offset="1" stop-color="#eed8cc"/></linearGradient>
      <linearGradient id="paleMid" x1="0" y1="0" x2="0" y2="1"><stop offset="0" stop-color="#fff"/><stop offset="1" stop-color="#e6e8ec"/></linearGradient>
    </defs>
    <rect x="244" y="0" width="245" height="330" fill="url(#paleMid)"/>
    <g role="img" aria-label="Young doctor showing a tablet to a smiling senior patient">
      <rect x="0" y="0" width="245" height="300" fill="url(#photoClinic)"/>
    </g>
    <g role="img" aria-label="Bandaged foot examined by a gloved hand holding a pen">
      <rect x="489" y="0" width="244" height="300" fill="url(#photoFoot)"/>
    </g>
    <path d="M0 276 C40 234,90 214,150 216 C220 220,260 274,320 299 C360 312,400 312,440 294 C500 264,540 219,610 214 C660 212,700 234,733 259 L733 517 L0 517Z" fill="var(--sky)"/>
    <path d="M0 284 C40 242,90 222,150 224 C220 228,260 282,320 307 C360 320,400 320,440 302 C500 272,540 227,610 222 C660 220,700 242,733 267 L733 517 L0 517Z" fill="url(#blueFill2)"/>
    <line x1="244.5" y1="0" x2="244.5" y2="517" stroke="#0a47a8" stroke-opacity=".15"/>
    <line x1="489" y1="0" x2="489" y2="517" stroke="#0a47a8" stroke-opacity=".15"/>
  </svg>

  <div class="block" style="left:258px;top:19px"><span class="pill pill--dark">Benefits and Challenges</span></div>
  <ul class="block ticks" style="left:258px;top:52px;width:220px;color:var(--ink)">
    <li style="margin-bottom:13px"><svg><use href="#tick-blue"/></svg><span>Why Patients Opt for In-Home Podiatry:</span></li>
    <li style="margin-bottom:13px"><svg><use href="#tick-blue"/></svg><span>Challenges in self foot-care due to impaired vision or reduced fine motor skills.</span></li>
    <li style="margin-bottom:13px"><svg><use href="#tick-blue"/></svg><span>Muscle weakness or dependency on mobility aids.</span></li>
    <li style="margin-bottom:13px"><svg><use href="#tick-blue"/></svg><span>Post-surgery restrictions, arthritis, or other health issues.</span></li>
    <li><svg><use href="#tick-blue"/></svg><span>Desire for Medicare-approved foot bath medication delivered to their door.</span></li>
  </ul>

  <div class="block" style="left:14px;top:286px"><span class="pill">Introduction</span></div>
  <ul class="block ticks on-blue" style="left:14px;top:321px;width:225px">
    <li style="margin-bottom:12.5px"><svg><use href="#tick-white"/></svg><span>Why In-Home Podiatry?</span></li>
    <li style="margin-bottom:12.5px"><svg><use href="#tick-white"/></svg><span>Difficulty visiting a podiatrist?</span></li>
    <li style="margin-bottom:12.5px"><svg><use href="#tick-white"/></svg><span>Need specialized foot and ankle care but limited by physical challenges?</span></li>
    <li style="margin-bottom:12.5px"><svg><use href="#tick-white"/></svg><span>Muscle weakness, walker, wheelchair, or post-surgery restrictions?</span></li>
    <li><svg><use href="#tick-white"/></svg><span>We are here for you! Offering specialized in-home podiatry services tailored for your unique needs.</span></li>
  </ul>

  <div class="block" style="left:258px;top:345px"><span class="pill">Introduction</span></div>
  <ul class="block ticks on-blue" style="left:258px;top:382px;width:225px">
    <li style="margin-bottom:12.5px"><svg><use href="#tick-white"/></svg><span>Care for a range of foot problems.</span></li>
    <li style="margin-bottom:12.5px"><svg><use href="#tick-white"/></svg><span>Relief for in-home caregivers.</span></li>
    <li style="margin-bottom:12.5px"><svg><use href="#tick-white"/></svg><span>Expertise in treating older patients.</span></li>
    <li><svg><use href="#tick-white"/></svg><span>Comprehensive evaluations and treatments.</span></li>
  </ul>

  <div class="block" style="left:502px;top:278px"><span class="pill">Service Details</span></div>
  <div class="block details" style="left:502px;top:313px;width:222px">
    <p>What to Expect During an In-Home Visit:</p>
    <p><b>Duration:</b>&nbsp; Typically 15-25 minutes.</p>
    <p><b>Examination:</b>&nbsp; Comprehensive check of feet, nails, skin, and potential infections.</p>
    <p><b>Evaluation:</b> Wound and pressure sore assessment, pulse checks, circulation signs, and nerve tests.</p>
    <p><b>Treatment:</b> Fungal toenail treatments, callus treatments, injections for arthritis, X-ray imaging (if needed), and more.</p>
  </div>
</section>
</body>
</html>
```